Menu Design Project

This is a sushi menu. We need to polish the menu. You can re-size logo and add color and graphic to make inviting. Please feel free to make any recommendations.

Upscale crowd

```html
<!DOCTYPE html>
<html lang="en">
<head>
<meta charset="utf-8">
<title>Koharu Sushi Bar — Menu</title>
<link rel="stylesheet" href="https://fonts.googleapis.com/css2?family=Oswald:wght@300;400;600;700&display=swap">
<style>
  :root {
    --red: #d42a2e;
    --ink: #1a1a1a;
    --muted: #6e6e6e;
    --special: #f29090;
    --special-ink: #ffffff;
    --band: #de5b5f;
    --blossom: #fbe3e3;
    --frame: #cfcfcf;
  }
  * { margin: 0; padding: 0; box-sizing: border-box; }
  html, body { width: 1200px; height: 1000px; overflow: hidden; background: #fff; }
  body { position: relative; font-family: "Oswald", sans-serif; color: var(--ink); }

  .menu-page {
    position: absolute; left: 288px; top: 25px; width: 634px; height: 952px;
    border: 1px solid var(--frame); background: #fff; overflow: hidden;
  }
  .blossom-backdrop {
    position: absolute; left: 200px; top: 0; width: 434px; height: 910px;
    background:
      radial-gradient(circle at 80% 8%, var(--blossom) 0, transparent 90px),
      radial-gradient(circle at 40% 22%, var(--blossom) 0, transparent 70px),
      radial-gradient(circle at 85% 55%, var(--blossom) 0, transparent 110px),
      radial-gradient(circle at 30% 62%, var(--blossom) 0, transparent 80px),
      radial-gradient(circle at 70% 88%, var(--blossom) 0, transparent 100px);
    opacity: .8;
  }

  .brand { position: absolute; left: 25px; top: 18px; width: 178px; text-align: center; }
  .brand-mark { display: block; width: 180px; height: 180px; margin: 0 auto; }
  .brand-name { font-weight: 700; font-size: 56px; line-height: 1; letter-spacing: 1px; margin-top: 12px; }
  .brand-sub { font-weight: 600; font-size: 19px; letter-spacing: 5.5px; margin-top: 6px; line-height: 1; }

  .section { position: absolute; width: 180px; }
  .section-title { font-weight: 700; font-size: 15px; letter-spacing: 9px; line-height: 1; margin-bottom: 12px; }
  .item { font-size: 6.6px; line-height: 10px; font-weight: 300; color: var(--muted); margin-bottom: 8px; letter-spacing: .5px; }
  .item b { font-weight: 600; color: var(--ink); margin-right: 4px; }
  .item .price { color: var(--ink); font-weight: 400; margin-left: 4px; }
  .item .opt { display: block; color: var(--ink); font-weight: 600; }
  .item .opt .price { margin-left: 3px; }
  .item.gap { margin-bottom: 16px; }

  .specials {
    position: absolute; left: 432px; top: 20px; width: 182px; height: 410px;
    background: var(--special); border-radius: 9px; padding: 16px 12px 0;
  }
  .specials .section-title { color: var(--special-ink); margin-bottom: 4px; }
  .specials .note { font-size: 6.6px; font-style: italic; font-weight: 300; color: var(--special-ink); margin-bottom: 12px; }
  .specials .item { color: var(--special-ink); letter-spacing: .3px; }
  .specials .item b, .specials .item .price, .specials .item .opt { color: var(--special-ink); }

  .footer-band {
    position: absolute; left: 0; bottom: 0; width: 100%; height: 42px; background: var(--band);
    color: #fff; font-size: 6.6px; font-style: italic; font-weight: 300; text-align: center;
    line-height: 10px; padding-top: 10px;
  }
</style>
</head>
<body>
<main class="menu-page">
  <div class="blossom-backdrop" role="img" aria-label="Faint pink cherry blossom branches in the background"></div>

  <header class="brand">
    <svg class="brand-mark" viewBox="0 0 180 180" aria-hidden="true"><circle cx="90" cy="90" r="89" fill="var(--red)"/></svg>
    <div class="brand-name">KOHARU</div>
    <div class="brand-sub">SUSHI BAR</div>
  </header>

  <section class="section" style="left:25px;top:306px">
    <h2 class="section-title">appetizers</h2>
    <p class="item"><b>edamame</b> soybeans &amp; seasalt <span class="price">3.5</span></p>
    <p class="item"><b>spicy garlic edamame</b> soybeans, seasalt &amp; spicy garlic <span class="price">4.5</span></p>
    <p class="item"><b>sautéed asparagus</b> asparagus &amp; teriyaki sauce <span class="price">4.5</span></p>
    <p class="item"><b>sautéed shiitake</b> mushrooms, onions &amp; cream sauce <span class="price">5</span></p>
    <p class="item"><b>age dashi tofu</b> tofu, sweet dashi soy sauce &amp; bonito flakes <span class="price">5</span></p>
    <p class="item"><b>yakitori</b> teriyaki chicken &amp; vegetables served on skewers <span class="price">6</span></p>
    <p class="item"><b>gyoza</b> beef &amp; vegetable dumplings <span class="price">5.5</span></p>
    <p class="item"><b>shumai</b> shrimp dumplings &amp; ponzu sauce <span class="price">5.5</span></p>
    <p class="item"><b>soft-shell crab</b> fried soft-shell crab &amp; ponzu sauce <span class="price">9</span></p>
    <p class="item"><b>tatsuta-age</b> panko breaded chicken, garlic<br>&amp; tempura sauce <span class="price">6</span></p>
    <p class="item"><b>tako su</b> octopus marinated in citrus sauce <span class="price">7</span></p>
    <p class="item"><b>calamari rings</b> fried calamari &amp; tempura sauce <span class="price">8</span></p>
    <p class="item"><b>grilled calamari</b> grilled calamari marinated in lemon teriyaki sauce, garlic &amp; ginger <span class="price">8</span></p>
    <p class="item"><b>hamachi kama</b> yellowtail collar &amp; ponzu sauce <span class="price">8</span></p>
    <p class="item"><b>mixed tempura</b> tempura shrimp &amp; vegetables <span class="price">7</span></p>
    <p class="item"><b>vegetable tempura</b> tempura vegetables <span class="price">6</span></p>
    <p class="item"><b>chicken katsu</b> breaded chicken skewers &amp; japanese barbecue sauce <span class="price">5.5</span></p>
  </section>

  <section class="section" style="left:25px;top:688px">
    <h2 class="section-title">soup</h2>
    <p class="item"><b>miso soup</b> tofu, scallions, seaweed &amp; miso broth <span class="price">2</span></p>
    <p class="item"><b>mushroom miso soup</b> tofu, scallions, enoki &amp; shiitake <span class="price">4</span></p>
    <p class="item"><b>suimono</b> japanese clear soup <span class="price">2</span></p>
    <p class="item"><b>ishikari nabe</b> salmon, miso broth &amp; vegetables <span class="price">8</span></p>
  </section>

  <section class="section" style="left:25px;top:804px">
    <h2 class="section-title">salads</h2>
    <p class="item"><b>house salad</b> mixed greens, vegetables &amp; ginger dressing <span class="price">2.5</span></p>
    <p class="item"><b>tofu salad</b> house salad, tofu, bonito flakes &amp; sesame dressing <span class="price">4</span></p>
    <p class="item"><b>seaweed salad</b> marinated seaweed, sesame seeds &amp; sesame oil <span class="price">4</span></p>
  </section>

  <section class="section" style="left:234px;top:25px">
    <p class="item"><b>spicy tuna salad*</b> spicy tuna, cucumber, masago, daikon, spring mix &amp; citrus sauce <span class="price">10</span></p>
    <p class="item"><b>crab salad</b> crab salad, cucumber, daikon, spring mix &amp; sesame dressing <span class="price">8</span></p>
    <p class="item"><b>spicy seafood salad*</b> shrimp, spicy scallop, crabstick, cucumber, daikon, spring mix &amp; sesame dressing <span class="price">10</span></p>
    <p class="item"><b>ika salad</b> squid salad &amp; japanese mountain vegetables <span class="price">6.5</span></p>
  </section>

  <section class="section" style="left:234px;top:145px">
    <h2 class="section-title">noodles</h2>
    <p class="item"><b>mori soba</b> chilled buckwheat noodles &amp; dipping sauce <span class="price">7</span></p>
    <p class="item"><b>tempura udon</b> japanese udon noodles, shrimp, seafood &amp; vegetable tempura <span class="price">10</span></p>
    <p class="item"><b>kake udon</b> japanese udon noodles, clear broth, scallions, seaweed, fried tofu &amp; fish cake <span class="price">7</span></p>
    <p class="item"><b>yaki udon</b> stir-fried chicken, cabbage, onions, scallions, carrots, bean sprouts &amp; seaweed flakes <span class="price">10</span></p>
    <p class="item"><b>vegetable udon</b> japanese udon noodles, vegetables, tofu &amp; clear broth <span class="price">8</span></p>
    <p class="item"><b>nabeyaki udon</b> japanese udon noodles, egg &amp; shrimp tempura <span class="price">11</span><span class="opt">add seafood <span style="font-weight:300">(mussle, shrimp, scallop &amp; calamari)</span><span class="price">13</span></span></p>
    <p class="item"><b>spicy seafood udon</b> sautéed shrimp, scallop, calamari, mussle, asparagus, zucchini &amp; carrots <span class="price">15</span></p>
    <p class="item"><b>yakisoba</b> stir-fried soba noodles &amp; vegetables<span class="opt">beef <span class="price">11</span></span><span class="opt">seafood <span style="font-weight:300">(shrimp, scallop &amp; calamari)</span><span class="price">14</span></span></p>
    <p class="item"><b>seafood noodle soup</b> noodle soup, vegetables, mussle, shrimp, scallop &amp; calamari <span class="price">11</span></p>
  </section>

  <section class="section" style="left:234px;top:444px">
    <h2 class="section-title">entrées</h2>
    <p class="item gap"><b>teriyaki</b> teriyaki sauce, sesame seeds &amp; vegetables served with a side of miso soup, house salad &amp; rice
      <span class="opt">salmon <span class="price">15</span></span><span class="opt">chicken <span class="price">12</span></span><span class="opt">beef <span class="price">15</span></span><span class="opt">beef &amp; chicken <span class="price">16</span></span><span class="opt">salmon w/ shrimp &amp; vegetable tempura <span class="price">17</span></span><span class="opt">chicken w/ shrimp &amp; vegetable tempura <span class="price">16</span></span><span class="opt">beef w/ shrimp &amp; vegetable tempura <span class="price">17</span></span></p>
    <p class="item gap"><b>katsu</b> breaded cutlet, japanese barbecue sauce &amp; shredded cabbage served with miso soup, house salad &amp; rice
      <span class="opt">chicken <span class="price">12</span></span><span class="opt">beef <span class="price">15</span></span><span class="opt">tonkatsu (porkloin) <span class="price">13</span></span><span class="opt">tonkatsu (porkloin) w/ shrimp &amp; vegetable tempura <span class="price">17</span></span></p>
    <p class="item gap"><b>tempura</b> lightly battered &amp; fried with a side of sauce served with miso soup, house salad &amp; rice
      <span class="opt">vegetable <span class="price">10</span></span><span class="opt">shrimp &amp; vegetable <span class="price">17</span></span></p>
    <p class="item gap"><b>negimaki</b> sliced meat, scallions &amp; teriyaki sauce served with a side of miso soup, house salad and rice
      <span class="opt">chicken <span class="price">12</span></span><span class="opt">beef <span class="price">15</span></span></p>
    <p class="item gap"><b>asparagus maki</b> sliced beef, asparagus &amp; teriyaki sauce served with a side of miso soup, house salad &amp; rice <span class="price">15</span></p>
    <p class="item gap"><b>bibimbap</b> rice, carrots, beansprouts, daikon, spinach, zucchini, sesame seeds, seaweed flakes, a side of spicy sauce &amp; your choice of raw or fried egg served with miso soup and salad
      <span class="opt">tofu <span class="price">11</span></span><span class="opt">chicken <span class="price">12</span></span><span class="opt">beef <span class="price">13</span></span></p>
    <p class="item"><b>bulgogi</b> thinly sliced beef, carrots &amp; onions served with a side of miso soup, house salad &amp; rice <span class="price">14</span></p>
  </section>

  <aside class="specials">
    <h2 class="section-title">specials</h2>
    <p class="note">lunch specials offered 11am-2:30pm, mon.-sat.</p>
    <p class="item"><b>chicken (9), beef or salmon teriyaki</b><span class="price">10</span></p>
    <p class="item"><b>tonkatsu <span style="font-weight:300">(porkloin)</span></b><span class="price">10</span></p>
    <p class="item"><b>shrimp &amp; vegetable tempura</b><span class="price">10</span></p>
    <p class="item"><b>chicken &amp; beef teriyaki</b><span class="price">11</span></p>
    <p class="item"><b>beef teriyaki w/ shrimp &amp; vegetable tempura</b><span class="price">11</span></p>
    <p class="item"><b>chicken teriyaki w/ shrimp &amp; vegetable tempura</b><span class="price">10</span></p>
    <p class="item"><b>salmon teriyaki w/ shrimp &amp; vegetable tempura</b><span class="price">11</span></p>
    <p class="item"><b>tonkatsu <span style="font-weight:300">(porkloin)</span> w/ shrimp &amp; vegetable tempura</b><span class="price">11</span></p>
    <p class="item"><b>bento box</b> fried rice, vegetable tempura, fruit, house special, miso soup &amp; house salad
      <span class="opt">beef teriyaki <span class="price">12</span></span><span class="opt">chicken teriyaki <span class="price">11</span></span><span class="opt">salmon teriyaki <span class="price">12</span></span><span class="opt">shrimp tempura <span class="price">11</span></span><span class="opt">chicken katsu <span class="price">11</span></span><span class="opt">tonkatsu (porkloin) <span class="price">11</span></span></p>
    <p class="item"><b>koharu box*</b> sashimi (2 pcs of each) salmon, tuna, red snapper, &amp; white tuna, nigiri (1 pc of each) inari, tamago &amp; shrimp, shrimp tempura roll (4 pcs) <span class="price">18</span></p>
    <p class="item"><b>omakase special*</b> nigiri (5 pcs) &amp; 1 california roll <span class="price">12</span></p>
    <p class="item"><b>omakase deluxe*</b> nigiri (5 pcs) &amp; 1 spicy tuna roll <span class="price">13</span></p>
    <p class="item"><b>maki combo*</b> california roll, cucumber roll &amp; tuna roll <span class="price">9</span></p>
    <p class="item"><b>maki combo special*</b> spicy tuna, avocado roll &amp; salmon roll <span class="price">10</span></p>
  </aside>

  <section class="section" style="left:444px;top:445px">
    <h2 class="section-title">sides</h2>
    <p class="item"><b>steamed rice</b><span class="price">1.5</span></p>
    <p class="item"><b>brown rice</b><span class="price">1.5</span></p>
    <p class="item"><b>sushi rice</b><span class="price">2</span></p>
    <p class="item"><b>avocado</b><span class="price">1.5</span></p>
    <p class="item"><b>tofu</b><span class="price">1</span></p>
    <p class="item"><b>shrimp tempura <span style="font-weight:300">(1pc.)</span></b><span class="price">2</span></p>
    <p class="item"><b>teriyaki sauce</b><span class="price">0.5</span></p>
    <p class="item"><b>ginger dressing</b><span class="price">0.5</span></p>
  </section>

  <section class="section" style="left:444px;top:632px">
    <h2 class="section-title">drinks (2)</h2>
    <p class="item"><b>house cola</b></p>
    <p class="item"><b>diet cola</b></p>
    <p class="item"><b>lemon soda</b></p>
    <p class="item"><b>orange soda</b></p>
    <p class="item"><b>orange or apple juice</b> (no refills)</p>
    <p class="item"><b>lemonade</b></p>
    <p class="item"><b>iced tea</b></p>
    <p class="item"><b>hot japanese green tea</b></p>
  </section>

  <section class="section" style="left:444px;top:821px">
    <h2 class="section-title">dessert</h2>
    <p class="item"><b>frushi</b> seasonal fruit wrapped in a maki roll <span class="price">8</span></p>
    <p class="item"><b>mochi ice cream</b> japanese confection w/ ice cream filling <span class="price">4</span></p>
  </section>

  <footer class="footer-band">
    *These foods contain raw seafood. Consuming raw or partially cooked seafood or shellfish may increase your chances of foodborne illness.<br>
    Prices &amp; availability subject to change. Special request will carry an additional charge.
  </footer>
</main>
</body>
</html>
```